Small Business Directory Site Requires a Professional Responsive Web Design

Small Business Directory and Coupon Site - we require a complete website design for a brand new responsive & mobile friendly website. We already have a coder who will professional code our website in Magento.

All PSD pages need to be professionally designed then uploaded into a sharedrive (i.e. like filemoor). Additionally, as I cannot pre-empt everything, please note that we may require a little more assistance once the files have been transferred (for example, in www.brambleleaf.com if you hover your mouse on the search box you will see a pop up box. We want one of these too and I think that means there may be extra design work here)

We have some draft page sketches have been created (there are some minor changes we want to the sketches provided though); however, we require an excellent designer to add the creative touches to it to make it look professionally created. All artwork/font must be legal.

-------------------------
We like the look of the www.brambleleaf.com and www. corvinlist.com

For the headers, please consider a font similar to TKV marigold. We likes this style, but it is too thin for the headers...so we need a variation like this one. For the copy/general text font, something basic that marries well with the headers.

---------------------

Please be sure to also read the brief we wrote for the coder as this will help with better understanding our design requirements.

In total I believe we have about 50 pages. This includes all the little pages and most of the pop up boxes (but not the little help key boxes). For example, pages include...

1. Login (this is where customers log in and can edit, manage their profiles. This means that there are backend membership pages)
2. Mini Services (same look and feel as the business coupons)
3. Resource Centre
4. Join (this is where customers learn about the packages available to submit a directory listing, if they ‘buy’ a package (i.e. free, $25 or $150 package) then they can create their own directory listing)
5. Search the directory (customer can view all the categories and also search the directory)
6. Create a directory listing (this is where customers learn about the packages available to submit a directory listing, if they ‘buy’ a package (i.e. free, $25 or $150 package) then they can create their own directory listing)
7. Quote finder (also know as Get a Quote)
8. Coupons (customer go to the business coupon page and can view all current coupons/submit a coupon)
9. Submit a coupon (form)
10.Advertise with us (form)
11. Join the forum
12.Submit an article or video (form)
13. Affiliates (listing of affiliates we currently have)
14. Become an affiliate (form)
15. Case studies (customer can view the case studies we have in the resource centre)
16. Help Guides (customer can view the help guides we have in the resource centre)
17. About Us
18 .Contact Us (form)
19. Terms & Condition
20. Privacy Policy
21. Supporting City Councils
22. Site Map
23. Forgot password / login details
24. Homepage
25. If we hover over a few areas (i.e. search box, location field) it pops up with more information.
etc etc etc. . . there are more pages.

Please see our filemoor link for the draft mock up pages that I have created so far.

https://www.filemoor.com/sh/qp71tkw4mzr8ab/XKLdWeNoVtQsFyGh2Ju5pcMRi

We are in a rush! We'd like to get the majority of the artwork completed by the end of the month. Minor fixes/tweaks can occur thereafter.

Target Market(s)

Small Businesses (employees 0 - 50) located throughout Australia

Industry/Entity Type

Business

Font styles to use
Sans Serif

Requirements
Must have
• Professional. Artwork must be legal (cannot be cut and paste or taken off other websites, must be legally purchased and used).Must look contemporary, fresh, modern.

Absolutely must be a responsive site!
Nice to have
• original work, original photos, original art.

like modern, fresh photos that demonstrate innovation, growth, small business, Australian scenery, stability, goals/passion.
Should not have
• cut and paste graphics, illegal graphics, not purchased graphics.

```html
<!DOCTYPE html>
<html lang="en">
<head>
<meta charset="utf-8">
<title>Tallowby Link — Small Business Directory</title>
<link rel="stylesheet" href="https://fonts.googleapis.com/css2?family=Montserrat:wght@400;500;600;700&family=Open+Sans:wght@400;600;700&display=swap">
<style>
:root{
  --black:#0b0b0b;
  --charcoal:#2b2b2b;
  --footer:#2e2e2e;
  --light:#e7e7e7;
  --white:#ffffff;
  --orange:#f47a20;
  --amber:#fcb317;
  --text:#3a3a3a;
  --muted:#9a9a9a;
  --line:#c9c9c9;
  --head:"Montserrat",sans-serif;
  --body:"Open Sans",sans-serif;
}
*{box-sizing:border-box;margin:0;padding:0}
html,body{width:1200px;height:2731px;overflow:hidden}
body{position:relative;font-family:var(--body);color:var(--text);background:var(--light)}
.abs{position:absolute}
section,header,footer{position:absolute;left:0;width:1200px}
a{color:inherit;text-decoration:none}

/* header */
.site-header{top:0;height:95px;background:var(--black)}
.brand{left:118px;top:24px;display:flex;align-items:center;gap:10px}
.brand-mark{width:44px;height:44px;background:var(--orange)}
.brand-name{font-family:var(--head);font-weight:600;font-size:27px;color:var(--white);letter-spacing:.5px}
.main-nav{right:118px;top:38px;display:flex;gap:0;font-family:var(--head);font-size:14px;color:var(--white)}
.main-nav a+ a::before{content:"|";margin:0 11px;color:#ccc}

/* hero */
.hero{top:95px;height:573px}
.hero-photo{position:absolute;inset:0;height:525px;background:linear-gradient(180deg,#bcd3dc 0%,#d9d2a4 35%,#c9a63a 62%,#8c6a16 100%)}
.hero-title{left:120px;top:170px;font-family:var(--head);font-size:30px;line-height:36px;color:var(--black);letter-spacing:.5px}
.hero-title b{font-weight:700}
.search-bar{left:124px;top:251px;width:593px;height:47px;border:4px solid var(--amber);background:var(--amber);display:flex;gap:4px}
.search-field{background:var(--white);display:flex;align-items:center;padding-left:38px;font-size:14px;color:#777;position:relative}
.search-field.what{width:213px}
.search-field.where{width:204px}
.search-field.where::after{content:"";position:absolute;right:16px;top:18px;border:5px solid transparent;border-top-color:#777}
.search-field svg{position:absolute;left:12px;top:11px}
.search-spacer{width:6px;background:var(--white);margin-left:-4px}
.search-btn{flex:1;background:var(--black);color:var(--white);font-family:var(--head);font-weight:600;font-size:15px;display:flex;align-items:center;justify-content:center}
.listing-promo{left:832px;top:129px;width:219px;height:277px;background:#e4e4e4}
.promo-head{position:absolute;left:0;top:0;width:219px;height:86px;background:var(--orange);border:2px dashed #ffb27a;outline:3px solid var(--orange);color:var(--white);font-family:var(--head);font-weight:700;font-size:16px;line-height:20px;text-align:center;padding-top:28px}
.promo-icon{position:absolute;left:91px;top:-14px;width:38px;height:38px;border-radius:50%;background:var(--orange);border:3px solid #fff0e4}
.promo-icon::after{content:"";position:absolute;left:10px;top:12px;width:12px;height:8px;background:var(--black)}
.promo-card{position:absolute;left:37px;top:100px;width:143px;height:164px;background:var(--white);border:2px solid var(--orange)}
.promo-price{height:31px;background:var(--orange);color:var(--white);font-family:var(--head);font-weight:700;font-size:17px;text-align:center;line-height:31px}
.promo-price small{font-size:10px}
.promo-card h4{font-family:var(--head);font-size:11px;font-weight:700;color:var(--black);padding:9px 10px 2px;line-height:14px}
.promo-card p{font-size:11px;line-height:15px;color:#555;padding:0 10px}
.promo-arrow{position:absolute;top:150px;font-size:34px;color:#666;font-family:var(--body);font-weight:400}
.category-bar{left:0;top:525px;width:1200px;height:48px;background:#1b1509;display:flex;align-items:center;padding-left:118px;font-family:var(--head);font-size:13.5px;color:var(--white)}
.category-bar span{margin-right:18px;display:flex;align-items:center}
.category-bar i{width:6px;height:6px;border-radius:50%;margin-right:7px;display:inline-block}
.view-all{position:absolute;right:118px;top:12px;width:79px;height:25px;background:var(--amber);color:var(--black);font-family:var(--head);font-weight:700;font-size:12px;text-align:center;line-height:25px}

/* offers */
.offers{top:668px;height:450px;background:var(--light)}
.section-title{width:100%;text-align:center;font-family:var(--head);font-weight:500;font-size:27px;color:var(--black)}
.offers .section-title{top:44px}
.offer-card{top:111px;width:221px;height:210px;background:var(--white)}
.offer-photo{position:absolute;left:11px;top:9px;width:199px;height:119px}
.offer-card h3{position:absolute;top:147px;width:100%;text-align:center;font-family:var(--head);font-weight:500;font-size:13.5px;color:#222}
.offer-card p{position:absolute;top:170px;width:100%;text-align:center;font-size:12px;line-height:15px;color:#555}
.slide-arrow{top:172px;font-size:40px;color:#555;font-weight:300}
.offers-rule{left:126px;top:388px;width:939px;height:1px;background:var(--line)}
.signup-label{left:380px;top:375px;width:210px;padding-right:14px;text-align:right;background:var(--light);font-size:14px;color:#444;line-height:26px}
.btn{position:absolute;display:flex;align-items:center;justify-content:center;font-family:var(--head);font-weight:600}
.btn-orange{background:var(--orange);color:var(--white)}
.btn-amber{background:var(--amber);color:var(--black)}
.submit-offer{left:594px;top:368px;width:180px;height:40px;font-size:16px}

/* directory band */
.directory{top:1118px;height:648px;background:var(--charcoal);color:var(--white)}
.directory .section-title{top:42px;color:var(--white);font-size:30px;font-weight:400}
.directory-sub{top:82px;width:100%;text-align:center;font-family:var(--head);font-size:22px;color:#b8b8b8}
.devices{left:131px;top:157px;width:534px;height:287px;background:linear-gradient(180deg,#4a4a4a,#111 70%,#2b2b2b);border-radius:8px}
.pitch{left:694px;font-size:14px;line-height:21px;color:var(--white);width:380px}
.pitch-head{left:694px;font-family:var(--head);font-size:18px;font-weight:500;color:var(--amber)}
.adv-btn{left:697px;width:133px;height:29px;font-size:13px}
.join-head{top:484px;width:100%;text-align:center;font-family:var(--head);font-weight:600;font-size:23px;color:var(--orange)}
.join-text{top:520px;width:100%;text-align:center;font-size:14px}
.join-btn{left:533px;top:563px;width:133px;height:29px;font-size:15px}

/* support */
.support{top:1766px;height:598px;background:var(--light)}
.support .section-title{top:36px}
.col-head{font-family:var(--head);font-size:19px;color:#333;top:127px}
.tab{top:164px;height:36px;display:flex;align-items:center;justify-content:center;font-family:var(--head);font-size:14px}
.tab-active{left:146px;width:220px;background:#222;color:var(--white)}
.tab-active::after{content:"";position:absolute;bottom:-9px;left:102px;border:8px solid transparent;border-top-color:#222;border-bottom:0}
.tab-idle{left:373px;width:197px;background:var(--white);color:#222}
.post-photo{left:146px;top:226px;width:193px;height:98px;background:linear-gradient(160deg,#8b8f7d,#4b4f42)}
.date-badge{background:var(--orange);color:var(--white);font-family:var(--head);font-weight:700;font-size:11.5px;text-align:center}
.post-photo .date-badge{position:absolute;right:0;bottom:0;width:62px;height:20px;line-height:20px}
.post-text{left:351px;top:230px;width:225px;font-size:13px;line-height:19px;color:#222}
.vault-rule{left:146px;width:430px;height:1px;background:var(--line)}
.event-row{left:146px;display:flex;align-items:center;gap:10px;font-size:12.5px;color:#222}
.event-row .date-badge{width:63px;height:20px;line-height:20px}
.vault-btn{left:146px;top:447px;width:173px;height:38px;font-size:14px}
.affiliate-photo{left:625px;top:157px;width:424px;height:197px;background:linear-gradient(135deg,#c8d6e2,#5f7286 55%,#2d3440)}
.affiliate-title{left:625px;top:368px;font-family:var(--head);font-weight:600;font-size:17px;color:var(--orange)}
.affiliate-text{left:625px;top:396px;width:430px;font-size:13px;line-height:19px;color:#333}
.brands-btn{left:625px;top:447px;width:171px;height:38px;font-size:14px}
.skyline{left:0;top:528px;width:1200px;height:70px;background:linear-gradient(180deg,rgba(160,160,160,0) 0%,#bdbdbd 75%,#b3b3b3 100%)}

/* footer */
.site-footer{top:2364px;height:367px;background:var(--footer);color:#d6d6d6}
.foot-col{top:52px}
.foot-col h5{font-family:var(--head);font-weight:700;font-size:14.5px;color:var(--white);margin-bottom:16px}
.foot-col ul{list-style:none;font-size:12.5px;line-height:26.8px}
.subscribe p{font-size:12.5px;line-height:21px;width:260px}
.sub-form{margin-top:14px;width:255px;height:34px;background:var(--white);display:flex;align-items:center;padding:0 4px 0 10px;font-size:11px;color:#aaa}
.sub-form span{flex:1}
.sub-form b{background:var(--amber);color:var(--black);font-family:var(--head);font-size:11px;padding:5px 8px}
.follow{margin-top:13px;display:flex;align-items:center;gap:16px;font-size:12px;font-style:italic;color:#ccc}
.follow i{width:14px;height:14px;border-radius:50%;background:#bbb;display:inline-block}
.foot-rule{left:107px;top:291px;width:986px;height:1px;background:#474747}
.copyright{top:320px;width:100%;text-align:center;font-size:12px;color:#ddd}
</style>
</head>
<body>

<header class="site-header">
  <div class="abs brand"><span class="brand-mark"></span><span class="brand-name">TALLOWBY LINK</span></div>
  <nav class="abs main-nav">
    <a href="#">Login</a><a href="#">Join</a><a href="#">Coupons</a><a href="#">Mini Service</a><a href="#">Get a Quote</a><a href="#">Advertise</a><a href="#">Resource Centre</a>
  </nav>
</header>

<section class="hero">
  <div class="hero-photo" role="img" aria-label="Sunlit Australian countryside with golden grass and scattered trees"></div>
  <h1 class="abs hero-title">IT’S A BRAND <b>NEW DAY</b><br>DO <b>MORE</b> OF WHAT YOU <b>LOVE</b></h1>
  <form class="abs search-bar">
    <div class="search-field what">
      <svg width="16" height="16" viewBox="0 0 16 16"><circle cx="8" cy="8" r="6.5" fill="none" stroke="#999" stroke-width="1.5"/></svg>
      What are your looking for
    </div>
    <div class="search-field where">
      <svg width="14" height="18" viewBox="0 0 14 18"><path d="M7 1a5.5 5.5 0 0 0-5.5 5.5C1.5 11 7 17 7 17s5.5-6 5.5-10.5A5.5 5.5 0 0 0 7 1z" fill="#aab"/><circle cx="7" cy="6.5" r="2" fill="#fff"/></svg>
      Where
    </div>
    <div class="search-spacer"></div>
    <div class="search-btn">Search</div>
  </form>
  <aside class="abs listing-promo">
    <div class="promo-head"><span class="promo-icon"></span>CREATE A DIRECTORY<br>LISTING TODAY</div>
    <span class="promo-arrow" style="left:10px">‹</span>
    <div class="promo-card">
      <div class="promo-price">A$25<small>/YEAR</small></div>
      <h4>2 CATERGORY<br>LITING</h4>
      <p>Promote you Spicial Offive Business Profile &amp; Logo websit &amp; Email Link</p>
    </div>
    <span class="promo-arrow" style="right:10px">›</span>
  </aside>
  <nav class="category-bar">
    <span><i style="background:#e8312f"></i>Banking</span>
    <span><i style="background:#2ea8e0"></i>Finance &amp; Insurance</span>
    <span><i style="background:#59b947"></i>Marketing</span>
    <span><i style="background:#f47a20"></i>Design</span>
    <span><i style="background:#fcb317"></i>Photography</span>
    <span><i style="background:#dddddd"></i>Video &amp; Print</span>
    <span><i style="background:#f47a20"></i>Coaching &amp; Technology</span>
    <a class="view-all" href="#">VIEW ALL</a>
  </nav>
</section>

<section class="offers">
  <h2 class="abs section-title">Featured Business Offers</h2>
  <span class="abs slide-arrow" style="left:82px">‹</span>
  <article class="abs offer-card" style="left:129px">
    <div class="offer-photo" role="img" aria-label="Customers at a service counter" style="background:linear-gradient(150deg,#c9b08d,#6e5640)"></div>
    <h3>JOIN MOBILE VERANO CLUB</h3><p>Text your name and number to<br>123123 to receive updates</p>
  </article>
  <article class="abs offer-card" style="left:368px">
    <div class="offer-photo" role="img" aria-label="Businessman facing a chalk wall of growth sketches" style="background:linear-gradient(150deg,#d4d4d4,#6a6a6a)"></div>
    <h3>JOIN MOBILE VERANO CLUB</h3><p>Text your name and number to<br>123123 to receive updates</p>
  </article>
  <article class="abs offer-card" style="left:606px">
    <div class="offer-photo" role="img" aria-label="Business team meeting in a bright office" style="background:linear-gradient(150deg,#e8eef2,#7b8fa0)"></div>
    <h3>JOIN MOBILE VERANO CLUB</h3><p>Text your name and number to<br>123123 to receive updates</p>
  </article>
  <article class="abs offer-card" style="left:845px">
    <div class="offer-photo" role="img" aria-label="Bicycle on a city street at night with bokeh lights" style="background:linear-gradient(150deg,#3b3550,#b5603a 60%,#2a2a2a)"></div>
    <h3>JOIN MOBILE VERANO CLUB</h3><p>Text your name and number to<br>123123 to receive updates</p>
  </article>
  <span class="abs slide-arrow" style="left:1099px">›</span>
  <div class="abs offers-rule"></div>
  <div class="abs signup-label">Signup for Daily Deals</div>
  <a class="btn btn-orange submit-offer" href="#">Submit An Offer</a>
</section>

<section class="directory">
  <h2 class="abs section-title">Australia’s Small Business Directory</h2>
  <p class="abs directory-sub">Free directory listing, business solution, business resources</p>
  <div class="abs devices" role="img" aria-label="Directory website shown on a desktop, tablet and phones"></div>
  <p class="abs pitch" style="top:168px">Do you sell a product or service? want to reach<br>Australian small business?</p>
  <a class="btn btn-amber adv-btn" style="top:224px" href="#">Advertise Now</a>
  <h3 class="abs pitch-head" style="top:279px">Submit an Offer</h3>
  <p class="abs pitch" style="top:310px">Do you sell a product or service? want to reach<br>Australian small business?</p>
  <a class="btn btn-amber adv-btn" style="top:366px" href="#">Advertise Now</a>
  <h3 class="abs join-head">Join Us</h3>
  <p class="abs join-text">We actively PROMOTE your business offer to our members</p>
  <a class="btn btn-orange join-btn" href="#">Join Free</a>
</section>

<section class="support">
  <h2 class="abs section-title">Get Real Support</h2>
  <h3 class="abs col-head" style="left:146px">FROM THE VAULT</h3>
  <div class="abs tab tab-active">Daily Events</div>
  <div class="abs tab tab-idle">Events Calender</div>
  <div class="abs post-photo" role="img" aria-label="Conference room with delegates around a long table"><span class="date-badge">21 JUNE</span></div>
  <p class="abs post-text">What is leadership? How does poor leadership affect business start of blog post or resource post to get them interesting in reading....</p>
  <div class="abs vault-rule" style="top:341px"></div>
  <div class="abs event-row" style="top:354px"><span class="date-badge">22 JUNE</span>Lorem Ipsum dolor sit amet and typesetting industry</div>
  <div class="abs vault-rule" style="top:386px"></div>
  <div class="abs event-row" style="top:400px"><span class="date-badge">26 JUNE</span>Lorem Ipsum dolor sit amet and typesetting industry</div>
  <a class="btn btn-amber vault-btn" href="#">VIEW ALL EVENTS</a>

  <h3 class="abs col-head" style="left:621px">OUR AFFILIATES</h3>
  <div class="abs affiliate-photo" role="img" aria-label="Business partners shaking hands in an office"></div>
  <h4 class="abs affiliate-title">AFFILIATE ABC BRAND</h4>
  <p class="abs affiliate-text">We are collaborating with networking groups around the country to bring our members more support and greater choice</p>
  <a class="btn btn-amber brands-btn" href="#">VIEW MORE BRANDS</a>
  <div class="abs skyline" role="img" aria-label="Silhouettes of Australian animals, trees and people along the horizon"></div>
</section>

<footer class="site-footer">
  <div class="abs foot-col" style="left:117px"><h5>SITE DIRECTORY</h5><ul>
    <li>Search the Directory</li><li>Create a Directory Listing</li><li>Quote Finder</li><li>Coupons</li><li>Submite A Coupons</li><li>Advertise with US</li></ul></div>
  <div class="abs foot-col" style="left:293px"><h5>RESOURCES</h5><ul>
    <li>Joine the forum</li><li>submit an Article or video</li><li>Affiliates</li><li>Become an Affiliate</li><li>Case Studies</li><li>Help Guides</li></ul></div>
  <div class="abs foot-col" style="left:466px"><h5>CATEGORIES</h5><ul>
    <li>Lorem ipsum dolor sit</li><li>consectetur adipiscing</li><li>elit, sed do eiusmod</li><li>tempor incididunt labore</li></ul></div>
  <div class="abs foot-col" style="left:641px"><h5>ABOUT</h5><ul>
    <li>About Us</li><li>Contact Us</li><li>Terms and Conditions</li><li>Privacy Policy</li><li>Supporting&nbsp; City Councils</li><li>Site map</li></ul></div>
  <div class="abs foot-col subscribe" style="left:825px"><h5>SUBSCRIBE US</h5>
    <p>Receive our latest offers, stories &amp; event news, direct to your inbox</p>
    <div class="sub-form"><span>Enter email address</span><b>SIGN UP</b></div>
    <div class="follow">Follow the site: <i></i><i></i><i></i><i></i></div>
  </div>
  <div class="abs foot-rule"></div>
  <p class="abs copyright">© 2014 Tallowby Link. All Rights Reserved</p>
</footer>

</body>
</html>
```